Dietitian needs awesome business card

I need a contemporary design that's eye catching but professional.
My card is to given to doctors, specialists and patients alike.
I manage patients with chronic diseases
I have uploaded my logo and current business card, I would also like the other Registered Clinical Nutritionist logo incorporated into the design

Target Market(s)

Doctors, specialists and patients

Industry/Entity Type

Healthcare

Contact Information for Business Card

www.brindlecovenutrition.com.au
Ph: 0427 516 903
Fax: 6482 7315
email: marcus.k.wellfare@quorvamail.com
Space on the back of the card with: Appointment date, Appointment time and appointment location

Font styles to use
Serif

Colors
fbee3e
876aae
ffc214

Requirements
Must have
• My Logo
• Registered Clinical Nutritionist Logo
• My 4 locations - Fernhollow Medical Centre, North Kelby Health, Ashcourt Medical, Pinebrook Doctors Surgery
Nice to have
• I like the colours in my current business card

```html
<!DOCTYPE html>
<html lang="en">
<head>
<meta charset="utf-8">
<title>Brindlecove Nutrition &amp; Dietetics – Business Card</title>
<link rel="stylesheet" href="https://fonts.googleapis.com/css2?family=Gelasio:wght@400;500;700&display=swap">
<style>
  :root {
    --stage: #ecebe7;
    --card: #fbfbfa;
    --blue: #2a3fa8;
    --blue-mid: #1e6fc0;
    --green: #9ac53a;
    --green-light: #b6d64a;
    --orange: #f0892b;
    --rule: #6b6f78;
    --text: #2c3a8c;
    --ink: #222;
  }
  * { box-sizing: border-box; margin: 0; padding: 0; }
  html, body { width: 1200px; height: 780px; overflow: hidden; }
  body {
    background: var(--stage);
    font-family: "Gelasio", Georgia, serif;
    position: relative;
  }
  .card {
    position: absolute;
    top: 230px;
    width: 540px;
    height: 320px;
    background: var(--card);
    border-radius: 14px;
    overflow: hidden;
    box-shadow: 0 6px 22px rgba(0,0,0,.18);
  }
  .card--front { left: 40px; }
  .card--back { left: 620px; }
  .card__bands { position: absolute; inset: 0; width: 540px; height: 320px; }

  /* Front */
  .social-square {
    position: absolute; top: 20px; right: 44px;
    width: 18px; height: 18px; border-radius: 3px; background: var(--blue-mid);
  }
  .cert-badge {
    position: absolute; top: 48px; right: 60px;
    width: 74px; height: 54px; border-radius: 4px; background: var(--orange);
  }
  .brand { position: absolute; left: 34px; top: 70px; display: flex; align-items: center; gap: 14px; }
  .brand__dot { width: 64px; height: 64px; border-radius: 50%; background: var(--blue-mid); }
  .brand__name { font-size: 48px; font-weight: 500; color: var(--blue); line-height: 1; }
  .brand__tag { font-size: 20px; color: var(--green); margin-top: 4px; }
  .person {
    position: absolute; left: 34px; top: 164px;
    font-size: 22px; font-weight: 700; color: var(--text);
  }
  .person-rule {
    position: absolute; left: 34px; top: 196px; width: 420px; height: 2px; background: var(--blue);
  }
  .contacts { position: absolute; left: 34px; top: 206px; list-style: none; }
  .contacts li {
    display: flex; align-items: center; gap: 8px;
    font-size: 15px; color: var(--ink); line-height: 22px;
  }
  .contacts svg { width: 16px; height: 16px; flex: none; }

  /* Back */
  .appt-title {
    position: absolute; left: 70px; top: 18px;
    font-size: 24px; font-weight: 400; color: var(--text);
  }
  .field { position: absolute; left: 70px; width: 440px; display: flex; align-items: flex-end; gap: 10px; color: var(--text); font-size: 15px; }
  .field__line { height: 1px; background: var(--rule); flex: 1; margin-bottom: 4px; }
  .field--title-line { top: 54px; }
  .field--location { top: 84px; }
  .field--date { top: 166px; }
  .field--time { top: 202px; }
  .field__ampm { font-size: 14px; line-height: 1.1; }
  .days { position: absolute; left: 70px; top: 122px; display: flex; gap: 22px; list-style: none; }
  .days li { display: flex; align-items: center; gap: 6px; color: var(--green); font-size: 14px; }
  .days li::before {
    content: ""; width: 18px; height: 18px; border: 1px solid var(--rule); background: #fff;
  }
  .locations { position: absolute; left: 70px; top: 252px; width: 440px; }
  .locations__label { font-size: 13px; font-weight: 700; color: var(--text); margin-bottom: 4px; }
  .locations__list {
    list-style: none; display: grid; grid-template-columns: 1fr 1fr;
    column-gap: 16px; row-gap: 2px; font-size: 13px; color: var(--ink);
  }
  .locations__list li::before { content: "• "; color: var(--green); }
</style>
</head>
<body>

<section class="card card--front" aria-label="Business card front">
  <svg class="card__bands" viewBox="0 0 540 320" aria-hidden="true">
    <defs>
      <linearGradient id="blueBand" x1="0" y1="0" x2="0" y2="1">
        <stop offset="0" stop-color="#2a3fa8"/><stop offset="1" stop-color="#1e6fc0"/>
      </linearGradient>
      <linearGradient id="greenBand" x1="0" y1="0" x2="0" y2="1">
        <stop offset="0" stop-color="#b6d64a"/><stop offset="1" stop-color="#9ac53a"/>
      </linearGradient>
    </defs>
    <path d="M512 0 H540 V150 L500 172 V0 Z" fill="url(#blueBand)"/>
    <path d="M470 196 L540 158 V320 H450 Z" fill="url(#greenBand)"/>
  </svg>
  <span class="social-square" aria-hidden="true"></span>
  <span class="cert-badge" aria-hidden="true"></span>

  <div class="brand">
    <span class="brand__dot" aria-hidden="true"></span>
    <div>
      <div class="brand__name">Brindlecove</div>
      <div class="brand__tag">Nutrition &amp; Dietetics</div>
    </div>
  </div>

  <div class="person">Marcus Wellfare</div>
  <div class="person-rule"></div>

  <ul class="contacts">
    <li>
      <svg viewBox="0 0 16 16" aria-hidden="true"><rect width="16" height="16" rx="3" fill="#1e6fc0"/><path d="M5 3.5 L7 6 L6 7.2 Q7.3 9.4 9 10.2 L10.2 9.2 L12.5 11 L11.5 12.6 Q7 12.5 3.6 5.2 Z" fill="#fff"/></svg>
      0427 516 903
    </li>
    <li>
      <svg viewBox="0 0 16 16" aria-hidden="true"><rect width="16" height="16" rx="3" fill="#1e6fc0"/><rect x="4" y="3" width="8" height="4" fill="#fff"/><rect x="3" y="7" width="10" height="6" rx="1" fill="#fff"/></svg>
      6482 7315
    </li>
    <li>
      <svg viewBox="0 0 16 16" aria-hidden="true"><rect width="16" height="16" rx="3" fill="#1e6fc0"/><rect x="3" y="4.5" width="10" height="7" fill="none" stroke="#fff"/><path d="M3 4.5 L8 9 L13 4.5" fill="none" stroke="#fff"/></svg>
      marcus.k.wellfare@quorvamail.com
    </li>
    <li>
      <svg viewBox="0 0 16 16" aria-hidden="true"><rect width="16" height="16" rx="3" fill="#1e6fc0"/><circle cx="8" cy="8" r="5" fill="none" stroke="#fff"/><path d="M3 8 H13 M8 3 V13" stroke="#fff"/></svg>
      www.brindlecovenutrition.com.au
    </li>
  </ul>
</section>

<section class="card card--back" aria-label="Business card back">
  <svg class="card__bands" viewBox="0 0 540 320" aria-hidden="true">
    <defs>
      <linearGradient id="greenBandBack" x1="0" y1="0" x2="0" y2="1">
        <stop offset="0" stop-color="#b6d64a"/><stop offset="1" stop-color="#9ac53a"/>
      </linearGradient>
      <linearGradient id="blueBandBack" x1="0" y1="0" x2="0" y2="1">
        <stop offset="0" stop-color="#1e6fc0"/><stop offset="1" stop-color="#2a3fa8"/>
      </linearGradient>
    </defs>
    <path d="M0 0 H28 V200 L0 214 Z" fill="url(#greenBandBack)"/>
    <path d="M0 232 L44 210 V320 H0 Z" fill="url(#blueBandBack)"/>
  </svg>

  <h2 class="appt-title">Has An Appointment On</h2>
  <div class="field field--title-line"><span class="field__line"></span></div>
  <div class="field field--location"><span>Location</span><span class="field__line"></span></div>
  <ul class="days">
    <li>Mon</li><li>Tues</li><li>Wed</li><li>Thur</li><li>Fri</li><li>Sat</li>
  </ul>
  <div class="field field--date"><span>Date</span><span class="field__line"></span></div>
  <div class="field field--time"><span>AT</span><span class="field__line"></span><span class="field__ampm">am.<br>pm.</span></div>

  <div class="locations">
    <p class="locations__label">Practice Locations</p>
    <ul class="locations__list">
      <li>Fernhollow Medical Centre</li>
      <li>North Kelby Health</li>
      <li>Ashcourt Medical</li>
      <li>Pinebrook Doctors Surgery</li>
    </ul>
  </div>
</section>

</body>
</html>
```